Tovrimel Complete Stationery - Logo already designed

I already have the logo designed see attached. I need have a full set of stationary and business card designed for printing. I have attached an example of what I mean.

Please feel free to be creative. Also you can use the X in the logo by its self if you think it will work.

My details:

Name: Dorian Pelsett
Social media handles: @dorianpelsett
W: dorianpelsett.com
E: info@dorianpelsett.com
​P: 08 7349 5286
PO Box 3872, Wendlemore 6047
ABN 83 274 908 615

Target Market(s)

Anyone looking to be inspired.

Industry/Entity Type

Business

Font styles to use
Sans Serif

Colors
fbee3e
000000

Requirements
Must have
• My details:
• Name: Dorian Pelsett
• Social media handles: @dorianpelsett
• W: dorianpelsett.com
• E: info@dorianpelsett.com
• ​P: 08 7349 5286
• PO Box 3872, Wendlemore 6047
• ABN 83 274 908 615
Nice to have
• Something a little different
Should not have
• must not look tacky.

```html
<!DOCTYPE html>
<html lang="en">
<head>
<meta charset="utf-8">
<title>Tovrimel Business Card</title>
<link rel="stylesheet" href="https://fonts.googleapis.com/css2?family=Open+Sans:wght@400;600;800&display=swap">
<style>
  :root {
    --backdrop: #4f4640;
    --card: #0d0d0d;
    --card-edge: #1a1a1a;
    --yellow: #fbee3e;
    --gold: #f2c40f;
    --white: #f4f4f4;
    --silver: #8e8e8e;
  }
  * { margin: 0; padding: 0; box-sizing: border-box; }
  html, body { width: 1200px; height: 1200px; overflow: hidden; }
  body {
    background: var(--backdrop);
    font-family: "Open Sans", sans-serif;
    display: flex;
    flex-direction: column;
    align-items: center;
    justify-content: center;
    gap: 60px;
  }
  .card {
    position: relative;
    width: 840px;
    height: 480px;
    background: var(--card);
    border: 1px solid var(--card-edge);
    box-shadow: 0 18px 40px rgba(0,0,0,0.45);
    overflow: hidden;
  }
  /* Front */
  .front .brand {
    position: absolute;
    left: 0; right: 0; top: 180px;
    text-align: center;
    font-weight: 800;
    font-size: 96px;
    letter-spacing: 2px;
    color: var(--white);
    text-transform: uppercase;
    line-height: 1;
  }
  .front .social {
    position: absolute;
    left: 200px; bottom: 70px;
    font-size: 20px;
    color: var(--white);
  }
  .front .social .label { color: var(--gold); }
  /* Back */
  .back .brand {
    position: absolute;
    left: 60px; top: 50px;
    font-weight: 800;
    font-size: 52px;
    letter-spacing: 1px;
    color: var(--silver);
    text-transform: uppercase;
    line-height: 1;
  }
  .back .company {
    position: absolute;
    left: 60px; top: 215px;
    font-size: 20px;
    line-height: 1.3;
    color: var(--white);
  }
  .back .contact-list {
    list-style: none;
    position: absolute;
    left: 60px; top: 290px;
    font-size: 20px;
    line-height: 1.3;
    color: var(--white);
  }
  .contact-list li { display: flex; align-items: center; gap: 10px; }
  .contact-list svg { width: 16px; height: 16px; fill: var(--gold); flex: none; }
  .back .person {
    position: absolute;
    right: 60px; bottom: 80px;
    text-align: right;
  }
  .person .name { font-size: 32px; font-weight: 600; color: var(--gold); line-height: 1.1; }
  .person .role { font-size: 21px; color: var(--white); }
</style>
</head>
<body>
  <section class="card front">
    <div class="brand">Tovrimel</div>
    <p class="social"><span class="label">Social media:</span> @dorianpelsett</p>
  </section>

  <section class="card back">
    <div class="brand">Tovrimel</div>
    <p class="company">ABN 83 274 908 615<br>PO Box 3872, Wendlemore 6047</p>
    <ul class="contact-list">
      <li>
        <svg viewBox="0 0 16 16" aria-hidden="true"><path d="M4 1c1 0 2 3 2 4s-1 1-1 2 2 4 3 4 1-1 2-1 4 1 4 2-1 3-3 3C6 15 1 10 1 4c0-2 2-3 3-3z"/></svg>
        <span>08 7349 5286</span>
      </li>
      <li>
        <svg viewBox="0 0 16 16" aria-hidden="true"><path d="M1 3h14v10H1z M2 4l6 5 6-5" fill="none" stroke="#f2c40f" stroke-width="1.6"/></svg>
        <span>info@dorianpelsett.com</span>
      </li>
      <li>
        <svg viewBox="0 0 16 16" aria-hidden="true"><g fill="none" stroke="#f2c40f" stroke-width="1.4"><circle cx="8" cy="8" r="6.5"/><ellipse cx="8" cy="8" rx="3" ry="6.5"/><path d="M1.5 8h13"/></g></svg>
        <span>www.dorianpelsett.com</span>
      </li>
    </ul>
    <div class="person">
      <div class="name">Dorian Pelsett</div>
      <div class="role">Director</div>
    </div>
  </section>
</body>
</html>
```